'Our Values' graphic

Hi there,
Could I get few options creating this graphic in a more minimalist, corporate look - using minimalist graphic elements and designs and using minimalist fonts (see tavlix or mundelo for inspiration)
I would also like the lines around the outside to be more minimalist. Maybe a thin line or a graphic element.
Change 'Core Values' title to 'Our Values'
Keep the font of 'Values'.
I would like to see a version in all dark grey and another version with the font in the lower square with each line of font being a different colour (Red, Blue, Green and Orange)

Requirements
Must have
• 'Our Values' and using the same font for 'Values' as the original artwork
Nice to have
• Minimalist artwork

```html
<!DOCTYPE html>
<html lang="en">
<head>
<meta charset="utf-8">
<title>Our Values</title>
<link href="https://fonts.googleapis.com/css2?family=Encode+Sans+Condensed:wght@500&display=swap" rel="stylesheet">
<style>
  :root {
    --backdrop: #a7a8ac;
    --brand-blue: #23abe2;
    --charcoal: #3a3a3c;
    --paper: #ffffff;
    --value-red: #ec1c24;
    --value-blue: #22aee4;
    --value-green: #1aa84b;
    --value-orange: #f7941d;
  }
  * { margin: 0; padding: 0; box-sizing: border-box; }
  html, body {
    width: 1200px;
    height: 710px;
    overflow: hidden;
    background: var(--backdrop);
  }
  .values-board {
    position: relative;
    width: 1200px;
    height: 710px;
  }
  .values-sign {
    position: absolute;
    top: 116px;
    width: 431px;
    height: 466px;
    border-radius: 10px;
    box-shadow: 14px 14px 18px rgba(0, 0, 0, 0.35);
    overflow: hidden;
  }
  .values-sign--blue { left: 130px; --accent: var(--brand-blue); }
  .values-sign--dark { left: 641px; --accent: var(--charcoal); }
  .sign-shapes {
    position: absolute;
    inset: 0;
    width: 100%;
    height: 100%;
  }
  .title-lettering {
    position: absolute;
    left: 90px;
    top: 25px;
    width: 252px;
    height: 140px;
    border-radius: 14px;
    background: linear-gradient(160deg, rgba(255, 255, 255, 0.95), rgba(255, 255, 255, 0.75));
  }
  .value-list {
    position: absolute;
    left: 45px;
    top: 254px;
    list-style: none;
    font-family: "Encode Sans Condensed", sans-serif;
    font-weight: 500;
    font-size: 36px;
    line-height: 47px;
    letter-spacing: -2px;
    color: var(--charcoal);
    white-space: nowrap;
  }
  .values-sign--dark .value-rise { color: var(--value-red); }
  .values-sign--dark .value-innovate { color: var(--value-blue); }
  .values-sign--dark .value-safety { color: var(--value-green); }
  .values-sign--dark .value-empower { color: var(--value-orange); }
</style>
</head>
<body>
<main class="values-board">

  <section class="values-sign values-sign--blue">
    <svg class="sign-shapes" viewBox="0 0 900 973" preserveAspectRatio="none" aria-hidden="true">
      <rect x="4" y="4" width="892" height="965" rx="18" fill="var(--paper)" stroke="var(--accent)" stroke-width="9"/>
      <polygon points="8,9 892,9 892,263 774,378 591,378 491,479 8,479" fill="var(--accent)"/>
      <polygon points="8,9 120,9 8,121" fill="var(--paper)"/>
    </svg>
    <div class="title-lettering" role="img" aria-label="Hand-lettered title reading Our Values, in white"></div>
    <ul class="value-list">
      <li class="value-rise">RISE TOGETHER</li>
      <li class="value-innovate">INNOVATE EDUCATION</li>
      <li class="value-safety">SAFETY FIRST</li>
      <li class="value-empower">EMPOWER CONNECTIONS</li>
    </ul>
  </section>

  <section class="values-sign values-sign--dark">
    <svg class="sign-shapes" viewBox="0 0 900 973" preserveAspectRatio="none" aria-hidden="true">
      <rect x="4" y="4" width="892" height="965" rx="18" fill="var(--paper)" stroke="var(--accent)" stroke-width="9"/>
      <polygon points="8,9 892,9 892,263 774,378 591,378 491,479 8,479" fill="var(--accent)"/>
      <polygon points="8,9 120,9 8,121" fill="var(--paper)"/>
    </svg>
    <div class="title-lettering" role="img" aria-label="Hand-lettered title reading Our Values, in white"></div>
    <ul class="value-list">
      <li class="value-rise">RISE TOGETHER</li>
      <li class="value-innovate">INNOVATE EDUCATION</li>
      <li class="value-safety">SAFETY FIRST</li>
      <li class="value-empower">EMPOWER CONNECTIONS</li>
    </ul>
  </section>

</main>
</body>
</html>
```